Home Loan Introducer needs logo/business cards

We need a simple but classy logo for business cards and flyers. The business is a home loan referral business that is called an Introducer. The business name is "The Pellgrove".
I was thinking very simple and straight to the point on the front with "Home Loans" the only thing on the front with a nice background colour/s.
Then on the back, "The Pellgrove"
and "Quality Customer Service"
and "Email, text or call welcome"
and then my name, email address and phone number.
Thank you for all the designs :-)
Home buyers.
Home owners.
Investors.
Loan

```html
<!DOCTYPE html>
<html lang="en">
<head>
<meta charset="utf-8">
<title>The Pellgrove — Business Card</title>
<link rel="stylesheet" href="https://fonts.googleapis.com/css2?family=League+Gothic&display=swap">
<style>
  :root {
    --page: #ffffff;
    --ink: #333333;
    --back-top: #f2f6d8;
    --back-bottom: #f6f6f2;
    --front-top: #c3f0da;
    --front-mid: #a2cfc2;
    --front-bottom: #6c8c95;
  }
  html, body {
    margin: 0;
    padding: 0;
    width: 1200px;
    height: 434px;
    overflow: hidden;
    background: var(--page);
  }
  .canvas {
    position: relative;
    width: 1200px;
    height: 434px;
    font-family: "League Gothic", "Oswald", sans-serif;
    color: var(--ink);
    text-transform: uppercase;
  }
  .card {
    position: absolute;
    top: 72px;
    width: 508px;
    height: 288px;
    overflow: hidden;
  }
  .card--back {
    left: 72px;
    background: linear-gradient(170deg, var(--back-top) 0%, #f7f8ea 50%, var(--back-bottom) 100%);
  }
  .card--front {
    left: 620px;
    background: linear-gradient(180deg, var(--front-top) 0%, var(--front-mid) 55%, var(--front-bottom) 100%);
  }
  .business-name {
    position: absolute;
    left: 18px;
    top: 18px;
    margin: 0;
    font-weight: 400;
    font-size: 98px;
    line-height: 1;
    letter-spacing: 0.5px;
  }
  .tagline {
    position: absolute;
    left: 18px;
    top: 104px;
    margin: 0;
    font-size: 38px;
    line-height: 1;
  }
  .contact {
    position: absolute;
    left: 18px;
    top: 146px;
    margin: 0;
    padding: 0;
    list-style: none;
    font-size: 25px;
    line-height: 31.5px;
  }
  .service-title {
    position: absolute;
    left: 0;
    right: 0;
    top: 165px;
    margin: 0;
    text-align: center;
    font-weight: 400;
    font-size: 106px;
    line-height: 1;
    letter-spacing: 1px;
  }
</style>
</head>
<body>
  <main class="canvas">
    <section class="card card--back" aria-label="Card back">
      <h1 class="business-name">The Pellgrove</h1>
      <p class="tagline">Quality Customer Service</p>
      <ul class="contact">
        <li>Email, text or call welcome</li>
        <li>Your Name</li>
        <li>123-456-7890</li>
        <li>email@email.com</li>
      </ul>
    </section>
    <section class="card card--front" aria-label="Card front">
      <h2 class="service-title">Home Loans</h2>
    </section>
  </main>
</body>
</html>
```